Coastal Bridge Alliance Web Design

I would like a web design for a conference. Registration, Form completion, Hotel, Speakers etc. See link for sample similar but not the same.
http://kbq-trust.example/pvrlo/index.php/contact-us
We would like the design to depict the colours of the logo which is attached. A banner of the website will be provided. We would like a transitioning space in the top and front page of the website for announcements and showcase of events. We would like custom prepared headers for each grouping, example, Sponsor, Venue, Discussion etc.

```html
<!DOCTYPE html>
<html lang="en">
<head>
<meta charset="utf-8">
<title>Coastal Bridge Alliance Conference</title>
<link rel="stylesheet" href="https://fonts.googleapis.com/css2?family=Open+Sans:wght@300;400;600;700&display=swap">
<style>
:root{
  --page-blue:#0f5c9e;
  --page-deep:#0a4a85;
  --brand-blue:#1a7fcf;
  --nav-blue:#1e82d2;
  --tile-blue:#1466ad;
  --tile-dark:#0f5596;
  --head-blue:#1b7bc4;
  --accent-orange:#f08a1c;
  --text-grey:#666;
  --text-dark:#333;
  --line:#dcdcdc;
  --white:#fff;
}
*{box-sizing:border-box;margin:0;padding:0}
html,body{width:1015px;height:1200px;overflow:hidden}
body{
  font-family:'Open Sans',sans-serif;
  background:radial-gradient(ellipse 75% 60% at 50% 35%,#3aa0f0 0%,#1a6fc0 45%,var(--page-deep) 100%);
  position:relative;color:var(--text-grey);
}
.sheet{position:absolute;left:83px;top:0;width:848px;height:1088px;background:var(--white)}
.brand{position:absolute;left:15px;top:34px;display:flex;align-items:center;gap:8px}
.brand-dot{width:30px;height:30px;border-radius:50%;background:var(--brand-blue)}
.brand-name{font-size:14px;font-weight:700;color:#c8202a;line-height:17px;width:180px}
.social{position:absolute;left:362px;top:54px;display:flex;align-items:center;gap:6px;font-size:10.5px;color:var(--text-dark)}
.social span.label{margin-right:2px}
.social i{display:block;width:27px;height:27px;border-radius:50%}
.call{position:absolute;left:684px;top:48px;display:flex;gap:12px;align-items:center}
.call-icon{width:35px;height:35px;border-radius:50%;background:var(--accent-orange);display:flex;align-items:center;justify-content:center}
.call small{display:block;font-size:10px;color:var(--text-dark)}
.call strong{display:block;font-size:14px;font-weight:400;color:var(--brand-blue)}
.nav{position:absolute;left:15px;top:112px;width:819px;height:36px;background:var(--nav-blue);border-bottom:3px solid #1266b0;display:flex;justify-content:space-around;align-items:center;box-shadow:0 8px 8px -6px rgba(0,0,0,.35)}
.nav a{color:var(--white);font-size:9.5px;text-decoration:none;letter-spacing:.2px}
.hero{position:absolute;left:15px;top:170px;width:819px;height:304px;background:linear-gradient(100deg,#d9c3b8 0%,#efe4de 30%,#b8a29a 55%,#8da4c2 80%,#c9d5e4 100%);box-shadow:0 9px 8px -6px rgba(0,0,0,.45)}
.hero-text{position:absolute;left:402px;top:122px;color:var(--white)}
.hero-text h2{font-size:22px;font-weight:700;letter-spacing:.3px}
.hero-text p{font-size:15px;font-weight:300;margin-top:2px}
.hero-arrows{position:absolute;right:16px;bottom:16px;display:flex;gap:1px}
.hero-arrows span{width:21px;height:20px;background:rgba(120,120,120,.5);color:#eee;font-size:12px;display:flex;align-items:center;justify-content:center}
.welcome{position:absolute;left:15px;top:506px;width:560px}
.welcome h3{font-size:22px;font-weight:300;color:#444}
.welcome h1{font-size:17px;font-weight:700;color:var(--head-blue);margin-top:6px}
.intro-photo{position:absolute;left:15px;top:581px;width:222px;height:152px;border:1px solid #ccc;padding:5px;background:#eee}
.intro-photo div{width:100%;height:100%;background:linear-gradient(90deg,#d8c8bb,#9a8f8a 50%,#3b3b42)}
.copy{font-size:9.5px;line-height:19.5px;color:var(--text-grey)}
.copy-side{position:absolute;left:258px;top:577px;width:315px}
.copy-full{position:absolute;left:17px;top:751px;width:565px}
.events{position:absolute;left:596px;top:519px;width:238px;height:337px;border:1px solid var(--line)}
.events h4{background:var(--nav-blue);color:var(--white);font-size:12px;font-weight:600;height:35px;line-height:35px;padding-left:18px;border-bottom:2px solid #1266b0}
.event{display:flex;gap:15px;padding:14px 14px 14px 15px;border-bottom:1px solid var(--line);height:94px}
.event .thumb{width:82px;height:65px;flex:none;background:linear-gradient(135deg,#c9b7a8,#5b5350)}
.event b{display:block;font-size:9px;font-weight:600;color:var(--text-dark)}
.event em{display:block;font-style:normal;font-size:9px;color:var(--brand-blue);margin-top:3px}
.event p{font-size:9px;line-height:16px;margin-top:2px}
.more{position:absolute;right:10px;bottom:12px;font-size:9.5px;color:var(--accent-orange);display:flex;align-items:center;gap:5px}
.tile{position:absolute;top:883px;width:263px;height:184px;background:var(--tile-blue);box-shadow:0 9px 8px -6px rgba(0,0,0,.4)}
.tile header{height:44px;background:var(--tile-dark);display:flex;align-items:center;gap:10px;padding-left:20px;color:var(--white);font-size:13px;font-weight:600}
.tile p{color:#e6f0fa;font-size:9.5px;line-height:19px;padding:12px 20px 0 23px}
.tile .btn{display:inline-block;margin:12px 0 0 23px;background:#0d4f8d;color:#4fa6ea;font-size:8.5px;padding:6px 14px}
.footer{position:absolute;top:1126px;left:0;width:1015px;text-align:center;color:var(--white)}
.footer nav{font-size:8px;display:flex;justify-content:center;gap:17px}
.footer p{font-size:7.5px;margin-top:12px}
</style>
</head>
<body>
<div class="sheet">
  <div class="brand"><span class="brand-dot"></span><span class="brand-name">Coastal Bridge Alliance Conference 2015</span></div>
  <div class="social"><span class="label">Connect with our social network :</span>
    <i style="background:#1f5ea8"></i><i style="background:#17649a"></i><i style="background:#3aa4d8"></i><i style="background:#333"></i></div>
  <div class="call">
    <div class="call-icon"><svg width="16" height="16" viewBox="0 0 24 24"><path fill="#fff" d="M6.6 10.8a15.1 15.1 0 0 0 6.6 6.6l2.2-2.2a1 1 0 0 1 1-.25 11.4 11.4 0 0 0 3.6.6 1 1 0 0 1 1 1V20a1 1 0 0 1-1 1A17 17 0 0 1 3 4a1 1 0 0 1 1-1h3.5a1 1 0 0 1 1 1c0 1.25.2 2.45.6 3.6a1 1 0 0 1-.25 1z"/></svg></div>
    <div><small>Call Us :</small><strong>( 4120 ) 555 0187</strong></div>
  </div>
  <nav class="nav"><a>HOME</a><a>CONFERENCE INFO</a><a>PROGRAMME</a><a>SPEAKERS</a><a>PRESENTATIONS</a><a>PHOTO GALLERY</a><a>CONTACT US</a></nav>
  <div class="hero" role="img" aria-label="Photo of a smiling woman applauding in a conference audience">
    <div class="hero-text"><h2>LOREM IPSUM IS SIMPLY</h2><p>DUMMY TEXT OF THE PRINTING AND TYPESETTING</p></div>
    <div class="hero-arrows"><span>&#8249;</span><span>&#8250;</span></div>
  </div>
  <div class="welcome"><h3>WELCOME TO</h3><h1>COASTAL BRIDGE ALLIANCE CONFERENCE</h1></div>
  <div class="intro-photo"><div role="img" aria-label="Photo of business delegates standing together"></div></div>
  <p class="copy copy-side">Lorem Ipsum is simply dummy text of the printing and typesetting industry. Lorem Ipsum has been the industry's standard dummy text ever since the 1500s, when an unknown printer took a galley of type and scrambled it to make a type specimen book. It has survived not only five centuries, but also the leap into electronic typesetting, remaining essentially unchanged. It was popularised in the 1960s with the release of Dryset sheets containing Lorem Ipsum passages, and more recently with desktop publishing software like Quillset Layout</p>
  <p class="copy copy-full">Lorem Ipsum is simply dummy text of the printing and typesetting industry. Lorem Ipsum has been the industry's standard dummy text ever since the 1500s, when an unknown printer took a galley of type and scrambled it to make a type specimen book. It has survived not only five centuries, but also the leap into electronic typesetting, remaining essentially unchanged. It was popularised in the 1960s with the release of Dryset sheets containing Lorem Ipsum passages, and more recently with desktop publishing software like Quillset Layout</p>
  <aside class="events">
    <h4>EVENTS</h4>
    <div class="event"><div class="thumb" role="img" aria-label="Photo of a group meeting around a table"></div><div><b>LOREM IPSUM IS SIMPLY</b><em>Posted on 27 May 2015</em><p>Lorem Ipsum is simply dummy text...</p></div></div>
    <div class="event"><div class="thumb" role="img" aria-label="Photo of a presenter speaking to a seated audience" style="background:linear-gradient(135deg,#dfe7ef,#7d8da0)"></div><div><b>LOREM IPSUM IS SIMPLY</b><em>Posted on 27 May 2015</em><p>Lorem Ipsum is simply dummy text...</p></div></div>
    <div class="event" style="border-bottom:0"><div class="thumb" role="img" aria-label="Photo of hands writing notes at a desk" style="background:linear-gradient(135deg,#2e3340,#a08a78)"></div><div><b>LOREM IPSUM IS SIMPLY</b><em>Posted on 27 May 2015</em><p>Lorem Ipsum is simply dummy text...</p></div></div>
    <div class="more">View more events <svg width="10" height="10" viewBox="0 0 10 10"><circle cx="5" cy="5" r="5" fill="#f08a1c"/><path d="M4 2.8 6.2 5 4 7.2" stroke="#fff" stroke-width="1.4" fill="none"/></svg></div>
  </aside>
  <section class="tile" style="left:15px"><header><svg width="26" height="22" viewBox="0 0 26 22"><circle cx="15" cy="6" r="4.5" fill="none" stroke="#fff" stroke-width="1.6"/><path d="M1 16h6l5 3h8l5-4-2-1-5 2h-5l-1-2h4v-2H8l-7 2z" fill="#fff"/></svg>SPONSOR</header>
    <p>Lorem Ipsum is simply dummy text of the printing and typesetting industry. Lorem Ipsum has been the industry's standard dummy text ever since the 1500s, when an unknown printer...</p><a class="btn">Read more</a></section>
  <section class="tile" style="left:294px"><header><svg width="22" height="26" viewBox="0 0 22 26"><path d="M11 2a7 7 0 0 0-7 7c0 5 7 12 7 12s7-7 7-12a7 7 0 0 0-7-7z" fill="none" stroke="#fff" stroke-width="1.8"/><circle cx="11" cy="9" r="2.5" fill="#fff"/><ellipse cx="11" cy="23" rx="8" ry="2" fill="none" stroke="#fff" stroke-width="1.4"/></svg>VENUE</header>
    <p>Lorem Ipsum is simply dummy text of the printing and typesetting industry. Lorem Ipsum has been the industry's standard dummy text ever since the 1500s, when an unknown printer...</p><a class="btn">Read more</a></section>
  <section class="tile" style="left:571px"><header><svg width="30" height="24" viewBox="0 0 30 24"><path d="M3 9c0-4 4-7 9-7s9 3 9 7-4 7-9 7l-5 3 1-4c-3-1-5-3-5-6z" fill="none" stroke="#fff" stroke-width="1.8"/><path d="M22 9c3 1 5 3 5 5.5 0 2-1 3.5-3 4.5l1 3.5-4-2.5c-3 0-5-1-6-2.5" fill="none" stroke="#fff" stroke-width="1.8"/></svg>DISCUSSION</header>
    <p>Lorem Ipsum is simply dummy text of the printing and typesetting industry. Lorem Ipsum has been the industry's standard dummy text ever since the 1500s, when an unknown printer...</p><a class="btn">Read more</a></section>
</div>
<footer class="footer">
  <nav><span>HOME</span><span>/</span><span>CONFERENCE INFO</span><span>/</span><span>PROGRAMME</span><span>/</span><span>SPEAKERS</span><span>/</span><span>PRESENTATIONS</span><span>/</span><span>PHOTO GALLERY</span><span>/</span><span>Contact us</span></nav>
  <p>COPYRIGHT © 2015. COASTAL BRIDGE ALLIANCE CONFERENCE. ALL RIGHTS RESERVED</p>
</footer>
</body>
</html>
```